Bright Path Trading
Business Cards and Stationary
Project: Bright Path Trading
Bright Path Trading -
Creative Brief
Modern
Rob and Kara Halvorsen, Owners
47 Elmcrest Road Northampton, MA 01384
rob@brightpathtrading.com
www.brightpathtrading.com
Please put Kara's email underneath Rob's email: kara@brightpathtrading.com

```html
<!DOCTYPE html>
<html lang="en">
<head>
<meta charset="utf-8">
<title>Bright Path Trading — Stationery</title>
<link rel="stylesheet" href="https://fonts.googleapis.com/css2?family=Open+Sans:wght@400;600;700&display=swap">
<style>
  :root {
    --bg: #e9e6e1;
    --paper: #ffffff;
    --maroon: #5b1a15;
    --green: #8cb42c;
    --lime: #c9dc3a;
    --green-deep: #6f9a1f;
    --ink: #4a3a34;
    --faint: #eeeadf;
    --shadow: 0 4px 14px rgba(0,0,0,.28);
  }
  * { box-sizing: border-box; margin: 0; padding: 0; }
  html, body { width: 1200px; height: 1094px; overflow: hidden; }
  body { background: var(--bg); font-family: "Open Sans", Arial, sans-serif; color: var(--ink); position: relative; }
  .piece { position: absolute; background: var(--paper); box-shadow: var(--shadow); overflow: hidden; }
  .swoosh { position: absolute; left: 0; bottom: 0; width: 100%; display: block; }
  .brand { font-family: "Open Sans", Arial, sans-serif; font-weight: 700; color: var(--maroon); white-space: nowrap; display: flex; align-items: center; gap: 8px; z-index: 2; }
  .brand-dot { width: 14px; height: 14px; border-radius: 50%; background: var(--green); flex: none; }
  .faint-mark { position: absolute; border-radius: 50%; background: var(--faint); z-index: 0; }
  .small { font-size: 9px; line-height: 1.45; z-index: 2; white-space: nowrap; }
  .small b { font-weight: 700; color: var(--maroon); }
  .web { position: absolute; color: #fff; font-size: 11px; font-weight: 600; letter-spacing: .3px; z-index: 2; }

  /* business card front */
  .card-front { left: 163px; top: 103px; width: 413px; height: 237px; }
  .card-front .brand { position: absolute; left: 22px; top: 20px; font-size: 19px; }
  .card-front .address { position: absolute; left: 22px; top: 56px; }
  .card-front .owners { position: absolute; left: 210px; top: 72px; z-index: 2; }
  .card-front .owners-name { font-size: 15px; font-weight: 700; color: var(--maroon); }
  .card-front .owners-role { font-size: 9px; }
  .card-front .contact { position: absolute; left: 22px; top: 100px; }
  .card-front .faint-mark { left: 300px; top: 10px; width: 70px; height: 70px; }
  .card-front .web { right: 22px; bottom: 18px; }

  /* business card back */
  .card-back { left: 163px; top: 384px; width: 413px; height: 237px;
    background: radial-gradient(circle at 50% 48%, var(--lime) 0%, var(--green) 55%, var(--green-deep) 100%); display: flex; align-items: center; justify-content: center; }
  .card-back .brand { color: #fff; font-size: 20px; }
  .card-back .brand-dot { background: #fff; }

  /* appointment card */
  .card-plain { left: 163px; top: 635px; width: 413px; height: 237px; display: flex; align-items: center; justify-content: center; }
  .card-plain .faint-mark { left: 110px; top: 50px; width: 130px; height: 130px; }
  .card-plain .brand-dot { width: 22px; height: 22px; position: relative; z-index: 2; }

  /* letterhead */
  .letterhead { left: 615px; top: 112px; width: 538px; height: 730px; }
  .letterhead .brand { position: absolute; left: 28px; top: 30px; font-size: 16px; gap: 6px; }
  .letterhead .brand .brand-dot { width: 11px; height: 11px; }
  .letterhead .header-info { position: absolute; right: 24px; top: 30px; font-size: 8px; }
  .letterhead .faint-mark { left: 250px; top: 330px; width: 200px; height: 200px; }
  .letterhead .web { right: 30px; bottom: 22px; }

  /* envelope front */
  .envelope { left: 65px; top: 842px; width: 526px; height: 222px; }
  .envelope .brand { position: absolute; left: 24px; top: 20px; font-size: 20px; }
  .envelope .address { position: absolute; left: 24px; top: 58px; }
  .envelope .faint-mark { left: 340px; top: 55px; width: 90px; height: 90px; }
  .envelope .web { right: 24px; bottom: 16px; }

  /* envelope back */
  .envelope-back { left: 615px; top: 857px; width: 538px; height: 192px; }
  .envelope-back .flap { position: absolute; inset: 0; width: 100%; height: 100%; }
  .envelope-back .brand-dot { position: absolute; left: 262px; top: 70px; }
</style>
</head>
<body>

<section class="piece card-front" aria-label="Business card front">
  <div class="faint-mark"></div>
  <div class="brand"><span class="brand-dot"></span>Bright Path Trading</div>
  <p class="small address">47 Elmcrest Road<br>Northampton, MA 01384</p>
  <div class="owners">
    <div class="owners-name">Rob and Kara Halvorsen</div>
    <div class="owners-role">Owners</div>
  </div>
  <p class="small contact"><b>Phone</b> (413) 555-0142<br><b>Fax</b> (413) 555-0143<br>rob@brightpathtrading.com<br>kara@brightpathtrading.com</p>
  <svg class="swoosh" viewBox="0 0 400 70" height="72" preserveAspectRatio="none" aria-hidden="true">
    <path d="M0 34 Q200 4 400 18 L400 70 L0 70 Z" fill="var(--maroon)"/>
    <path d="M0 24 Q200 -6 400 8 L400 20 Q200 6 0 36 Z" fill="var(--green)"/>
    <path d="M0 18 Q190 -10 400 0 L400 8 Q200 -2 0 26 Z" fill="var(--lime)"/>
  </svg>
  <span class="web">www.brightpathtrading.com</span>
</section>

<section class="piece card-back" aria-label="Business card back">
  <div class="brand"><span class="brand-dot"></span>Bright Path Trading</div>
</section>

<section class="piece card-plain" aria-label="Appointment card">
  <div class="faint-mark"></div>
  <span class="brand-dot"></span>
</section>

<section class="piece letterhead" aria-label="Letterhead">
  <div class="brand"><span class="brand-dot"></span>Bright Path Trading</div>
  <p class="small header-info">47 Elmcrest Road, Northampton, MA 01384<br><b>Phone</b> (413) 555-0142 | <b>Fax</b> (413) 555-0143<br><b>Email</b> rob@brightpathtrading.com | kara@brightpathtrading.com</p>
  <div class="faint-mark"></div>
  <svg class="swoosh" viewBox="0 0 400 70" height="100" preserveAspectRatio="none" aria-hidden="true">
    <path d="M0 34 Q200 4 400 18 L400 70 L0 70 Z" fill="var(--maroon)"/>
    <path d="M0 24 Q200 -6 400 8 L400 20 Q200 6 0 36 Z" fill="var(--green)"/>
    <path d="M0 18 Q190 -10 400 0 L400 8 Q200 -2 0 26 Z" fill="var(--lime)"/>
  </svg>
  <span class="web">www.brightpathtrading.com</span>
</section>

<section class="piece envelope" aria-label="Envelope front">
  <div class="faint-mark"></div>
  <div class="brand"><span class="brand-dot"></span>Bright Path Trading</div>
  <p class="small address">47 Elmcrest Road, Northampton, MA 01384<br><b>Phone</b> (413) 555-0142 | <b>Fax</b> (413) 555-0143<br><b>Email</b> rob@brightpathtrading.com</p>
  <svg class="swoosh" viewBox="0 0 400 70" height="70" preserveAspectRatio="none" aria-hidden="true">
    <path d="M0 34 Q200 4 400 18 L400 70 L0 70 Z" fill="var(--maroon)"/>
    <path d="M0 24 Q200 -6 400 8 L400 20 Q200 6 0 36 Z" fill="var(--green)"/>
    <path d="M0 18 Q190 -10 400 0 L400 8 Q200 -2 0 26 Z" fill="var(--lime)"/>
  </svg>
  <span class="web">www.brightpathtrading.com</span>
</section>

<section class="piece envelope-back" aria-label="Envelope back">
  <svg class="flap" viewBox="0 0 538 192" preserveAspectRatio="none" aria-hidden="true">
    <path d="M0 0 L269 110 L538 0" fill="none" stroke="#d8d4cc" stroke-width="1.5"/>
  </svg>
  <span class="brand-dot"></span>
</section>

</body>
</html>
```